Business Card Design

I need a business card designed for my new company BrightOak Home developments I specialise in all aspects of carpentry including Decks, Pergolas, Conventional Framing and fit outs I am open to different colours as long as it fits with my logo.

Industry/Entity Type

Carpentry

Contact Information for Business Card

BrightOak Home Developments, Greg Mollory, 0461802394, specialising in all aspects of carpentry and construction

```html
<!DOCTYPE html>
<html lang="en">
<head>
<meta charset="utf-8">
<title>BrightOak Home Developments — Business Card</title>
<link href="https://fonts.googleapis.com/css2?family=Lato:wght@400&display=swap" rel="stylesheet">
<style>
  :root {
    --page: #eeeeee;
    --frame-grey: #8a8a8a;
    --brand-blue: #3754a0;
    --paper: #ffffff;
    --ink: #333333;
    --ink-soft: #555555;
  }
  * { margin: 0; padding: 0; box-sizing: border-box; }
  html, body {
    width: 991px; height: 1200px; overflow: hidden;
    background: var(--page);
    font-family: "Lato", "Helvetica Neue", Arial, sans-serif;
  }
  .canvas { position: relative; width: 991px; height: 1200px; }
  .card {
    position: absolute; left: 64px; width: 870px; height: 520px;
    box-shadow: 0 4px 14px rgba(0,0,0,0.25);
  }
  .card--front { top: 63px; }
  .card--back { top: 618px; }
  .card__frame { position: absolute; inset: 0; display: block; }

  .brand {
    position: absolute; display: flex; align-items: center;
    color: var(--brand-blue); font-weight: 400;
  }
  .brand__mark { background: var(--brand-blue); flex: none; }
  .brand__text { display: flex; flex-direction: column; line-height: 1; }
  .brand__name { letter-spacing: 0.02em; text-transform: uppercase; }
  .brand__tagline { letter-spacing: 0.08em; text-transform: uppercase; }

  .card--front .brand { left: 110px; top: 205px; gap: 26px; }
  .card--front .brand__mark { width: 70px; height: 70px; }
  .card--front .brand__name { font-size: 62px; }
  .card--front .brand__tagline { font-size: 30px; margin-top: 10px; }

  .card--back .brand { left: 90px; top: 120px; gap: 18px; }
  .card--back .brand__mark { width: 44px; height: 44px; }
  .card--back .brand__name { font-size: 40px; }
  .card--back .brand__tagline { font-size: 20px; margin-top: 7px; }

  .contact {
    position: absolute; left: 193px; top: 318px; width: 560px;
    color: var(--ink); font-size: 20px;
  }
  .contact__row { display: flex; justify-content: space-between; align-items: center; }
  .contact__item { display: flex; align-items: center; gap: 6px; }
  .contact__icon { width: 16px; height: 18px; fill: var(--ink); }
  .contact__item--phone { margin-right: 18px; }
  .contact__tagline {
    margin-top: 8px; font-size: 19.5px; color: var(--ink-soft);
    text-decoration: underline; text-underline-offset: 4px;
  }
</style>
</head>
<body>
<main class="canvas">

  <section class="card card--front" aria-label="Business card front">
    <svg class="card__frame" viewBox="0 0 870 520" aria-hidden="true">
      <rect width="870" height="520" fill="var(--frame-grey)"/>
      <polygon points="665,0 870,0 870,205" fill="var(--brand-blue)"/>
      <line x1="655" y1="-5" x2="875" y2="215" stroke="var(--paper)" stroke-width="8"/>
      <polygon points="0,325 0,520 195,520" fill="var(--brand-blue)"/>
      <line x1="-5" y1="315" x2="205" y2="525" stroke="var(--paper)" stroke-width="8"/>
      <rect x="45" y="44" width="781" height="433" fill="var(--paper)"/>
    </svg>
    <div class="brand">
      <span class="brand__mark" aria-hidden="true"></span>
      <div class="brand__text">
        <span class="brand__name">BrightOak</span>
        <span class="brand__tagline">Home Developments</span>
      </div>
    </div>
  </section>

  <section class="card card--back" aria-label="Business card back">
    <svg class="card__frame" viewBox="0 0 870 520" aria-hidden="true">
      <rect width="870" height="520" fill="var(--frame-grey)"/>
      <polygon points="665,0 870,0 870,205" fill="var(--brand-blue)"/>
      <line x1="655" y1="-5" x2="875" y2="215" stroke="var(--paper)" stroke-width="8"/>
      <polygon points="0,262 0,520 258,520" fill="var(--brand-blue)"/>
      <line x1="-5" y1="252" x2="268" y2="525" stroke="var(--paper)" stroke-width="8"/>
      <rect x="42" y="42" width="786" height="436" fill="var(--paper)"/>
      <polygon points="42,262 42,478 258,478" fill="var(--brand-blue)"/>
      <line x1="37" y1="252" x2="268" y2="483" stroke="var(--paper)" stroke-width="8"/>
    </svg>
    <div class="brand">
      <span class="brand__mark" aria-hidden="true"></span>
      <div class="brand__text">
        <span class="brand__name">BrightOak</span>
        <span class="brand__tagline">Home Developments</span>
      </div>
    </div>
    <div class="contact">
      <div class="contact__row">
        <span class="contact__item">
          <svg class="contact__icon" viewBox="0 0 16 20" aria-hidden="true">
            <path d="M8 0C3.6 0 0 3.4 0 7.6 0 13 8 20 8 20s8-7 8-12.4C16 3.4 12.4 0 8 0zm0 10.6a3 3 0 1 1 0-6 3 3 0 0 1 0 6z"/>
          </svg>
          Greg Mollory
        </span>
        <span class="contact__item contact__item--phone">
          <svg class="contact__icon" viewBox="0 0 16 20" aria-hidden="true">
            <path d="M4 1c1.2-.6 2 0 2.4 1l1 3c.3.9-.2 1.5-1 2l-.8.5c.5 2 1.4 3.7 2.8 5.2l.9-.3c.9-.3 1.6 0 2 .8l1.2 2.6c.4 1-.1 1.7-1 2.2-3 1.3-6-2-7.5-5.5C2.6 8.9 1.6 2.3 4 1z"/>
          </svg>
          0461802394
        </span>
      </div>
      <p class="contact__tagline">specialising in all aspects of carpentry and construction</p>
    </div>
  </section>

</main>
</body>
</html>
```